Ferris Contracting LLC Business Card Design

I am looking for a creative and unique business card design. We are a commercial construction general contractor. With the name "FERRIS" Contracting, I am hoping to see some neat designs that correlate with the name.

```html
<!DOCTYPE html>
<html lang="en">
<head>
<meta charset="utf-8">
<title>Ferris Contracting LLC – Business Card</title>
<link rel="stylesheet" href="https://fonts.googleapis.com/css2?family=Arimo:wght@400;700&display=swap">
<style>
  :root {
    --backdrop: #5a5a5a;
    --charcoal: #2e2e2e;
    --blue-deep: #0f72b9;
    --blue-mid: #1f8ccf;
    --blue-glow: #38ace4;
    --brand-blue: #2b93dc;
    --brand-ice: #86e8fa;
    --silver-light: #e4e4e4;
    --silver-dark: #8c8c8c;
    --white: #ffffff;
  }
  * { box-sizing: border-box; margin: 0; padding: 0; }
  html, body {
    width: 1200px;
    height: 1200px;
    overflow: hidden;
    background: var(--backdrop);
    font-family: "Arimo", Arial, sans-serif;
  }
  .canvas {
    position: relative;
    width: 1200px;
    height: 1200px;
  }
  .card {
    position: absolute;
    width: 690px;
    height: 394px;
    overflow: hidden;
  }
  .card--front { left: 266px; top: 158px; display: flex; }
  .card--back {
    left: 260px; top: 651px;
    background: radial-gradient(ellipse 60% 70% at 50% 50%, var(--blue-glow) 0%, var(--blue-mid) 55%, var(--blue-deep) 100%);
  }
  .front__brand-panel {
    position: relative;
    width: 361px;
    height: 100%;
    background: var(--charcoal);
  }
  .front__divider {
    width: 9px;
    height: 100%;
    background: linear-gradient(90deg, var(--silver-dark), var(--silver-light) 45%, var(--silver-dark));
  }
  .front__info-panel {
    position: relative;
    flex: 1;
    height: 100%;
    background: radial-gradient(ellipse 70% 60% at 55% 50%, var(--blue-glow) 0%, var(--blue-mid) 55%, var(--blue-deep) 100%);
    color: var(--white);
    padding: 92px 0 0 23px;
  }
  .wordmark {
    position: absolute;
    display: flex;
    align-items: center;
    gap: 10px;
    transform: translate(-50%, -50%);
    white-space: nowrap;
    font-weight: 700;
    letter-spacing: 1px;
  }
  .wordmark__dot {
    width: 14px; height: 14px;
    border-radius: 50%;
    background: currentColor;
  }
  .wordmark--front { left: 180px; top: 197px; font-size: 23px; color: var(--brand-blue); }
  .wordmark--back  { left: 345px; top: 197px; font-size: 34px; color: var(--brand-ice); }
  .holder__name { font-size: 27px; font-weight: 700; line-height: 1; letter-spacing: 0.3px; }
  .holder__title { font-size: 15px; margin-top: 6px; }
  .address { font-size: 16px; line-height: 21px; margin-top: 21px; }
  .contacts { list-style: none; margin-top: 12px; }
  .contacts li {
    display: flex;
    align-items: center;
    gap: 8px;
    font-size: 16.5px;
    line-height: 20.5px;
  }
  .contacts svg { width: 14px; height: 14px; flex: none; fill: var(--white); }
</style>
</head>
<body>
<div class="canvas">

  <section class="card card--front" aria-label="Business card front">
    <div class="front__brand-panel">
      <div class="wordmark wordmark--front"><span class="wordmark__dot"></span>FERRIS CONTRACTING</div>
    </div>
    <div class="front__divider"></div>
    <div class="front__info-panel">
      <h1 class="holder__name">DANIEL REYES</h1>
      <p class="holder__title">President</p>
      <p class="address">4120 Cedar Ridge Road<br>Fairview, Canada 58210</p>
      <ul class="contacts">
        <li>
          <svg viewBox="0 0 16 16" aria-hidden="true"><path d="M3.6 1.2l2.3 2.6-1.3 1.7c.9 2 2.5 3.6 4.5 4.6l1.7-1.3 2.6 2.3-1.2 2.4C8 13.4 2.4 8 1.3 3.2z"/></svg>
          <span>555-214-7730</span>
        </li>
        <li>
          <svg viewBox="0 0 16 16" aria-hidden="true"><path d="M4.5 0.5h7a1 1 0 0 1 1 1v13a1 1 0 0 1-1 1h-7a1 1 0 0 1-1-1v-13a1 1 0 0 1 1-1zm.4 1.6v10h6.2v-10zM8 12.8a.9.9 0 1 0 0 1.8.9.9 0 0 0 0-1.8z"/></svg>
          <span>555-389-1046</span>
        </li>
        <li>
          <svg viewBox="0 0 16 16" aria-hidden="true"><path d="M1 3.5h14v9H1zm1.6 1.2L8 9l5.4-4.3zm-.4 1.3v5.3l3.4-2.6zm11.6 0l-3.4 2.7 3.4 2.6z"/></svg>
          <span>info@ferriscontracting.com</span>
        </li>
        <li>
          <svg viewBox="0 0 16 16" aria-hidden="true"><path d="M8 1a7 7 0 1 0 0 14A7 7 0 0 0 8 1zm-1 2.2c-.6 1 .4 1.5-.5 2.3-.9.8-2.3.3-2.5 1.6-.2 1.2 1.2 1.4 1.8 2.3.6 1-.4 2.1.4 3.1-2.2-.8-3.6-3.1-3.2-5.6C3.3 4.9 5 3.5 7 3.2zm3.2.6c1.6.9 2.7 2.6 2.7 4.6l-1.4-.6c-.6-.3-1-.9-1.7-.6-.7.3-.4 1.4-1.2 1.6-.8.2-1.1-.8-.8-1.5.4-.8 1.6-.7 1.8-1.6.2-.7.5-1.2.6-1.9z"/></svg>
          <span>www.ferriscontracting.com</span>
        </li>
      </ul>
    </div>
  </section>

  <section class="card card--back" aria-label="Business card back">
    <div class="wordmark wordmark--back"><span class="wordmark__dot"></span>FERRIS CONTRACTING</div>
  </section>

</div>
</body>
</html>
```